Harlow Mesa Podiatry
Business card, letterhead & envelope
Professional
4631 NW 52nd St
Suite 310
Brookvale, GA 32786
mtollanddpm@brindlemail.com
Front of Card should also have names of doctors:
Marcus Tolland, DPM
Lanh T. Vu, DPM
Back of card should have information for appointment:
1. Date
2. Time
3. Day of week to circle (ie Mon, Tues, Wed, Thurs, Fri)
4. "If unable to keep appointment kindly give 24 hours notice"
Logo designs for Harlow Mesa Podiatry

```html
<!DOCTYPE html>
<html lang="en">
<head>
<meta charset="utf-8">
<title>Harlow Mesa Podiatry — Stationery</title>
<link href="https://fonts.googleapis.com/css2?family=Arimo:wght@400;700&display=swap" rel="stylesheet">
<style>
  :root {
    --green: #6cb33f;
    --green-dark: #4f8f2a;
    --ink: #2b2b2b;
    --grey: #6d6d6d;
    --paper: #ffffff;
    --shadow: rgba(0,0,0,0.18);
  }
  * { box-sizing: border-box; margin: 0; padding: 0; }
  html, body { width: 1200px; height: 923px; overflow: hidden; background: var(--paper); }
  body { position: relative; font-family: "Arimo", Arial, sans-serif; color: var(--ink); }

  .sheet { position: absolute; background: var(--paper); box-shadow: 0 1px 6px var(--shadow); }

  .brand { display: flex; align-items: center; gap: 8px; }
  .brand-mark { background: var(--green); flex: none; }
  .brand-name { font-weight: 700; color: var(--ink); line-height: 1.05; text-transform: uppercase; }

  .foot-art { position: absolute; border-radius: 45% 55% 40% 50%;
    background: linear-gradient(160deg, #fbfbfb, #f1f1f1); }

  .bar { height: 5px; background: var(--green); }
  .phone { display: inline-flex; align-items: center; gap: 3px; }

  /* Letterhead */
  .letterhead { left: 20px; top: 163px; width: 563px; height: 732px; }
  .letterhead .brand { position: absolute; left: 18px; top: 20px; }
  .letterhead .brand-mark { width: 34px; height: 34px; }
  .letterhead .brand-name { font-size: 16px; width: 110px; }
  .letterhead .doctors { position: absolute; left: 18px; top: 117px; font-size: 10px; line-height: 15px; color: var(--grey); }
  .letterhead .foot-art { left: 250px; top: 300px; width: 300px; height: 390px; }
  .letterhead .footer { position: absolute; left: 0; right: 0; bottom: 14px; display: flex; align-items: center; gap: 8px; font-size: 9px; color: var(--ink); white-space: nowrap; }
  .letterhead .footer .bar.lead { width: 12px; }
  .letterhead .footer .bar.trail { flex: 1; }

  /* Card front */
  .card-front { left: 600px; top: 188px; width: 243px; height: 142px; }
  .card-front .brand { position: absolute; left: 12px; top: 12px; gap: 5px; }
  .card-front .brand-mark { width: 20px; height: 20px; }
  .card-front .brand-name { font-size: 9px; width: 74px; }
  .card-front .doctors { position: absolute; left: 12px; top: 56px; font-size: 6.5px; line-height: 10px; color: var(--green-dark); text-transform: uppercase; }
  .card-front .address { position: absolute; left: 132px; top: 14px; font-size: 6.5px; line-height: 10px; color: var(--grey); }
  .card-front .contact { position: absolute; left: 132px; top: 102px; font-size: 6.5px; color: var(--ink); }
  .card-front .bar { position: absolute; left: 0; right: 0; bottom: 0; height: 6px; }

  /* Card back */
  .card-back { left: 858px; top: 188px; width: 242px; height: 142px; background: var(--green); }
  .card-back .foot-art { left: 14px; top: 20px; width: 34px; height: 92px; background: linear-gradient(160deg, #7ebf55, #5aa030); }
  .card-back .brand-name { position: absolute; left: 58px; top: 18px; font-size: 17px; width: 120px; }
  .card-back .days { position: absolute; right: 18px; top: 14px; list-style: none; font-size: 6px; color: var(--paper); }
  .card-back .days li { display: flex; align-items: center; gap: 4px; height: 14px; }
  .card-back .days li::before { content: ""; width: 9px; height: 9px; background: var(--paper); }
  .card-back .fields { position: absolute; left: 58px; top: 96px; display: flex; gap: 14px; font-size: 6px; }
  .card-back .fields span { display: inline-block; width: 48px; border-bottom: 1px solid var(--ink); margin-left: 3px; }
  .card-back .notice { position: absolute; left: 0; right: 0; bottom: 8px; text-align: center; font-size: 5.5px; color: var(--paper); }

  /* Envelope */
  .envelope { position: absolute; left: 555px; top: 375px; width: 603px; height: 388px; }
  .envelope svg.flap { position: absolute; left: 0; top: 0; }
  .envelope .body { left: 0; top: 125px; width: 603px; height: 263px; }
  .envelope .brand { position: absolute; left: 16px; top: 14px; }
  .envelope .brand-mark { width: 28px; height: 28px; }
  .envelope .brand-name { font-size: 13px; width: 110px; }
  .envelope .doctors { position: absolute; left: 16px; top: 56px; font-size: 6.5px; color: var(--grey); }
  .envelope .footer { position: absolute; left: 0; right: 0; bottom: 10px; display: flex; align-items: center; gap: 6px; font-size: 6.5px; white-space: nowrap; }
  .envelope .footer .bar.lead { width: 8px; height: 4px; }
  .envelope .footer .bar.trail { flex: 1; height: 4px; }
  .envelope .flap-art { position: absolute; left: 286px; top: 14px; width: 28px; height: 50px; border-radius: 40%; background: linear-gradient(160deg, #8ac666, #6cb33f); }
</style>
</head>
<body>

<section class="sheet letterhead">
  <div class="brand">
    <div class="brand-mark"></div>
    <div class="brand-name">Harlow Mesa Podiatry</div>
  </div>
  <p class="doctors">Marcus Tolland, DPM<br>Lanh T. Vu, DPM</p>
  <div class="foot-art" role="img" aria-label="Faint line drawing of a foot and lower leg"></div>
  <div class="footer">
    <span class="bar lead"></span>
    <span>4631 NW 52nd St | Suite 310 | Brookvale, GA 32786 |
      <span class="phone"><svg width="9" height="9" viewBox="0 0 10 10"><path d="M2 1l2 2-1 1.5a6 6 0 0 0 2.5 2.5L7 6l2 2-1.5 1.5C4 9 1 6 .5 2.5Z" fill="#2b2b2b"/></svg>(470) 555-0148</span></span>
    <span class="bar trail"></span>
  </div>
</section>

<section class="sheet card-front">
  <div class="brand">
    <div class="brand-mark"></div>
    <div class="brand-name">Harlow Mesa Podiatry</div>
  </div>
  <p class="doctors">Marcus Tolland, DPM<br>Lanh T. Vu, DPM</p>
  <p class="address">4631 NW 52nd St<br>Suite 310<br>Brookvale, GA 32786</p>
  <p class="contact"><span class="phone"><svg width="7" height="7" viewBox="0 0 10 10"><path d="M2 1l2 2-1 1.5a6 6 0 0 0 2.5 2.5L7 6l2 2-1.5 1.5C4 9 1 6 .5 2.5Z" fill="#2b2b2b"/></svg>(470) 555-0148</span></p>
  <span class="bar"></span>
</section>

<section class="sheet card-back">
  <div class="foot-art" role="img" aria-label="Outline drawing of a foot"></div>
  <div class="brand-name">Harlow Mesa Podiatry</div>
  <ul class="days">
    <li>Mon</li><li>Tue</li><li>Wed</li><li>Thu</li><li>Fri</li>
  </ul>
  <div class="fields">
    <p>Date<span></span></p>
    <p>Time<span></span></p>
  </div>
  <p class="notice">If unable to keep appointment kindly give 24 hours notice</p>
</section>

<section class="envelope">
  <svg class="flap" width="603" height="130" viewBox="0 0 603 130">
    <path d="M0 128 L286 4 Q301 -2 316 4 L603 118 L603 130 L0 130 Z" fill="#6cb33f" stroke="#4f8f2a" stroke-width="2"/>
  </svg>
  <div class="flap-art" role="img" aria-label="Small foot sketch on the envelope flap"></div>
  <div class="sheet body">
    <div class="brand">
      <div class="brand-mark"></div>
      <div class="brand-name">Harlow Mesa Podiatry</div>
    </div>
    <p class="doctors">Marcus Tolland, DPM — Lanh T. Vu, DPM</p>
    <div class="footer">
      <span class="bar lead"></span>
      <span>4631 NW 52nd St | Suite 310 | Brookvale, GA 32786 | (470) 555-0148</span>
      <span class="bar trail"></span>
    </div>
  </div>
</section>

</body>
</html>
```